Business Card and Letterhead for Juniper Anvil - (Have Logo)

Update 4: Removed company reg no from business card details as it looked a bit out of place. Updated services list.
UPDATE 3
Sorry, I got the address a little bit wrong, have updated it below. Sorry for any inconvenience caused.
UPDATE 2
Finally I have the details for the business cards and letterhead. Submissions already made do not have to be updated unless shortlisted, if all new submissions could include the details for me, Marcus, that would be very much appreciated and help with the final shortlist selection. I intend to share a shortlist of the three best entries with past and existing customers for their feedback and opinions. Thank you all again for your time.
Here are the details.
Marcus Telby
Web Developer
T: 01632 960 418
E: marcus@juniperanvil.example
www.juniperanvil.example
Professional Photography
Web Solutions & E-Commerce
Audio & HD Video Production
Marketing & Promotions
Identity and Branding
Juniper Anvil Ltd
Suite 20938, 3rd Floor
212-224 Orchard Lane
London, N7 9QX
Company Reg. No: 05829147
The order and the layout of the information are of course down to the design, but the company registration number should be smaller and less prominent. The formatting of the telephone and email address using a T: and an E: I am not sure about and again if it is Tel: or Email: or Icons is up to the design.
The Company No. on the letterhead should read (somewhere in small text along the bottom):
Juniper Anvil is a Ltd Company registered in England & Wales, Registration No. 05829147.
The second business card details are
Oliver Brackley
Photographer
T: 01632 960 418
E: oliver@juniperanvil.example
Everything else the same of course.
Thank you again for all the submissions so far.
END OF UPDATE 2
-
UPDATE 1: Please do not alter the logo nor the logo colours. (This was a previous pixel forum project and I am extremely happy with it. The icon can stand alone of course, but I have had to eliminate all entries that have made it black and white, or reversed the icon.) I would like to thank everyone that has participated so far and am very grateful for all your thought and time.
End of Update 1
-
Original Brief:
I have attached the logo vector file.
Following a superb logo from a previous Pixel Forum project I am now looking for a business card design and (although less important) a letterhead as well.
I must admit I tried to do it myself but could only come up with the usual amateur stuff that in comparison to the quality of the logo looked awful.
About Us
Juniper Anvil Ltd will be a new company due to start in January. It is really just me (a web developer) and my friend (a photographer). We will be aiming at the usual small to medium sized businesses in the local area, selling various digital services including photographic services to the public, web hosting and development, commercial photography, modelling services (not us!), full video and film production and possibly a bit of marketing as well. (Really it is anything we can do professionally all lumped together! We met running seperate businesses which have both since closed)
We will not be competing on price. We plan to be expensive but fair. Certainly not the cheapest.
What we are looking for
Business Card
I imagine a double sided business card, which will be used for more than one person. I imagine the front to be the same for everyone and the persons details to be on the back, although this is of course only my thoughts and I am of course completely open to any ideas.
The card could also have a services list or a bit about what we do on it. It might feature the website address, our business address (mail forwarding address) or our registered company number.
Or it might have none of that, we are completely open to any ideas and have no real fixed opinions. I just want it to be really nice :-)
Letterhead (secondary importance)
We will make our decision primarily on the business card, although a mathcing letterhead would be fantastic. Something standardish in format and simple, although again, all ideas are welcomed.
I hope that is enough information but if you have any questions I will answer them as fully and as quickly as possible.
Thank you once again and I really look forward to seeing your ideas and picking a winner.
Marcus T.
Small businesses AND the general public
Film Production

```html
<!DOCTYPE html>
<html lang="en">
<head>
<meta charset="utf-8">
<title>Juniper Anvil – Business Card Concepts</title>
<link rel="stylesheet" href="https://fonts.googleapis.com/css2?family=Source+Sans+3:ital,wght@0,400;0,600;0,700;1,700&display=swap">
<style>
  :root {
    --brand-red: #c4161c;
    --ink: #1a1a1a;
    --ink-soft: #333333;
    --card-edge: #4a4a4a;
    --tint-pink: #f7e0d9;
    --tint-grey: #ececec;
    --paper: #ffffff;
  }
  * { box-sizing: border-box; margin: 0; padding: 0; }
  html, body {
    width: 1200px; height: 930px; overflow: hidden;
    background: var(--paper);
    font-family: "Source Sans 3", "Myriad Pro", Arial, sans-serif;
    color: var(--ink);
  }
  .sheet { position: relative; width: 1200px; height: 930px; }

  .card {
    position: absolute; background: var(--paper);
    border: 1.5px solid var(--card-edge); overflow: hidden;
  }
  .card--portrait { width: 260px; height: 451px; left: 4px; }
  .card--marcus { top: 4px; }
  .card--oliver { top: 478px; }
  .card--company { left: 451px; top: 86px; width: 455px; height: 260px; }

  .card__tint { position: absolute; inset: 0; width: 100%; height: 100%; }

  .brand {
    position: absolute; display: flex; align-items: center; gap: 8px;
    color: var(--brand-red); font-weight: 700; text-transform: uppercase;
    letter-spacing: 0.04em; white-space: nowrap;
  }
  .brand__mark { width: 20px; height: 20px; background: var(--brand-red); flex: none; }
  .card--portrait .brand { top: 16px; left: 12px; font-size: 26px; }

  .person { position: absolute; left: 38px; width: 140px; top: 93px; text-align: center; }
  .person__name { font-size: 18px; font-weight: 600; line-height: 22px; }
  .person__role { font-size: 11.5px; line-height: 15px; color: var(--ink-soft); }

  .services {
    position: absolute; left: 13px; top: 192px; list-style: none;
    font-size: 14px; font-weight: 700; font-style: italic; line-height: 21.5px;
  }

  .contact { position: absolute; right: 10px; top: 395px; text-align: right; font-size: 14px; line-height: 25px; }

  .card--company .brand {
    left: 16px; bottom: 14px; font-size: 25px;
    writing-mode: vertical-rl; transform: rotate(180deg);
  }
  .company { position: absolute; left: 226px; top: 14px; }
  .company__name { font-size: 17px; font-weight: 400; line-height: 24px; }
  .company__address { font-size: 17px; font-weight: 600; line-height: 25px; }
  .company__web { position: absolute; left: 226px; top: 139px; font-size: 14px; }
  .company__tel { position: absolute; left: 226px; top: 208px; font-size: 14px; }

  .note {
    position: absolute; left: 487px; top: 517px;
    font-size: 33px; line-height: 44.5px; color: var(--ink); white-space: nowrap;
  }
</style>
</head>
<body>
<main class="sheet">

  <article class="card card--portrait card--marcus">
    <svg class="card__tint" viewBox="0 0 260 451" aria-hidden="true">
      <rect x="0" y="70" width="40" height="381" fill="var(--tint-grey)"/>
      <rect x="0" y="150" width="40" height="90" fill="var(--tint-pink)"/>
      <rect x="0" y="330" width="40" height="90" fill="var(--tint-pink)"/>
      <rect x="150" y="70" width="40" height="381" fill="var(--tint-grey)"/>
      <rect x="150" y="110" width="40" height="90" fill="var(--tint-pink)"/>
      <rect x="150" y="290" width="40" height="90" fill="var(--tint-pink)"/>
      <rect x="40" y="150" width="110" height="40" fill="var(--tint-pink)" opacity="0.6"/>
      <rect x="190" y="230" width="70" height="40" fill="var(--tint-pink)" opacity="0.6"/>
    </svg>
    <div class="brand"><span class="brand__mark"></span>Juniper Anvil</div>
    <div class="person">
      <p class="person__name">Marcus Telby</p>
      <p class="person__role">Web Developer</p>
    </div>
    <ul class="services">
      <li>professional photography</li>
      <li>web solutions &amp; e-commerce</li>
      <li>audio &amp; HD video production</li>
      <li>marketing &amp; promotion</li>
      <li>identity &amp; branding</li>
    </ul>
    <div class="contact">
      <p>Tel: 01632 960 418</p>
      <p>marcus@juniperanvil.example</p>
    </div>
  </article>

  <article class="card card--company">
    <svg class="card__tint" viewBox="0 0 455 260" aria-hidden="true">
      <rect x="72" y="6" width="375" height="96" fill="var(--tint-pink)" opacity="0.7"/>
      <rect x="72" y="110" width="375" height="50" fill="var(--tint-grey)"/>
      <rect x="72" y="168" width="375" height="70" fill="var(--tint-pink)" opacity="0.7"/>
    </svg>
    <div class="brand"><span class="brand__mark"></span>Juniper Anvil</div>
    <div class="company">
      <p class="company__name">Juniper Anvil Ltd</p>
      <p class="company__address">Suite 20938, 3rd Floor</p>
      <p class="company__address">212-224 Orchard Lane</p>
      <p class="company__address">London, N7 9QX</p>
    </div>
    <p class="company__web">www.juniperanvil.example</p>
    <p class="company__tel">Tel: 01632 960 418</p>
  </article>

  <article class="card card--portrait card--oliver">
    <svg class="card__tint" viewBox="0 0 260 451" aria-hidden="true">
      <rect x="0" y="70" width="40" height="381" fill="var(--tint-grey)"/>
      <rect x="0" y="150" width="40" height="90" fill="var(--tint-pink)"/>
      <rect x="0" y="330" width="40" height="90" fill="var(--tint-pink)"/>
      <rect x="150" y="70" width="40" height="381" fill="var(--tint-grey)"/>
      <rect x="150" y="110" width="40" height="90" fill="var(--tint-pink)"/>
      <rect x="150" y="290" width="40" height="90" fill="var(--tint-pink)"/>
      <rect x="40" y="150" width="110" height="40" fill="var(--tint-pink)" opacity="0.6"/>
      <rect x="190" y="230" width="70" height="40" fill="var(--tint-pink)" opacity="0.6"/>
    </svg>
    <div class="brand"><span class="brand__mark"></span>Juniper Anvil</div>
    <div class="person">
      <p class="person__name">Oliver Brackley</p>
      <p class="person__role">Photographer</p>
    </div>
    <ul class="services">
      <li>professional photography</li>
      <li>web solutions &amp; e-commerce</li>
      <li>audio &amp; HD video production</li>
      <li>marketing &amp; promotion</li>
      <li>identity &amp; branding</li>
    </ul>
    <div class="contact">
      <p>Tel: 01632 960 418</p>
      <p>oliver@juniperanvil.example</p>
    </div>
  </article>

  <p class="note">
    The black outline is just that an outline.<br>
    These cards are 2 x 3.5 without any bleeds or<br>
    trim lines. I am not sure if you need a different<br>
    size or not.&nbsp; If you use my design I can give<br>
    you a copy which has bleed and trim lines or<br>
    you can get dimensions from your printer.<br>
    Also, I can put the phone number on the<br>
    front also, if you want.
  </p>

</main>
</body>
</html>
```